Sexy Flyer for Bra Sale

We a need flyer designed for promoting the brand Tarvel Apparel Company which has just begun selling bra's. need a flyer which can posted on Facebook and other social media websites. the flyer has to be attractive to girls/ladies between the ages 16 - 39. The company has been associated mainly with men's products and is now venturing into supplying bra's into the market. The tarvel company logo, the bra label design and the pictures of the bra's are attached.

Product description
Microfiber T-shirt bra with molded, lightly padded underwire cups for shaping and good support the bra also give's a fuller, uplifted shape and enhanced cleavage . Invisible seams for improved comfort. Narrow, adjustable shoulder straps and hook-and-eye fasteners at back. Available in two colors of Black & Black with Decorative Touches of Pink.

About Tarvel Apparel Company
The Tarvel Apparel Company was founded on the philosophy of design, quality and the ideals of redefining fashion. Sri Lanka is the global hub for manufacturing some of the most exclusive and fashionable products and the Tarvel brand aims at giving the Sri Lankan consumer access to high-quality, affordable and fashionable clothing from a trusted company and name. A company-wide devotion to high quality‚ honest values and timeless style with a twist. That’s authentic Tarvel. And that’s just what you’ll get‚ no matter your latitude or longitude. At Tarvel Apparel Company we constantly strive to build a culture just as inspiring as the people who wear our clothes…

Target Market(s)

Ladies Girls 16 -39
Selling Bra's

Industry/Entity Type

Womens Clothing

Requirements
Must have
• To be able to upload the flyer on Facebook and other social media platforms
• the flyer must include the Tarvel Apparel Company Logo
Nice to have
• Sexy flyer.

```html
<!DOCTYPE html>
<html lang="en">
<head>
<meta charset="utf-8">
<title>Tarvel Apparel Company – Invisible Seams Flyer</title>
<link rel="stylesheet" href="https://fonts.googleapis.com/css2?family=Lato:wght@300;400;700;900&display=swap">
<style>
  :root {
    --pink: #e97aa3;
    --pink-soft: #f3a9c4;
    --plum: #4a4558;
    --ink: #2f2c36;
    --paper: #ffffff;
    --curtain: #f1f0ef;
    --skin: #d9b49c;
  }
  * { box-sizing: border-box; margin: 0; padding: 0; }
  html, body { width: 907px; height: 1200px; overflow: hidden; background: var(--paper); }
  body { font-family: "Lato", Arial, sans-serif; color: var(--ink); }

  .flyer { position: relative; width: 907px; height: 1200px; background: var(--paper); overflow: hidden; }

  .hero-photo {
    position: absolute; left: 0; top: 0; width: 907px; height: 560px;
    background:
      radial-gradient(ellipse 190px 300px at 300px 300px, var(--skin) 0%, rgba(217,180,156,0.55) 55%, rgba(241,240,239,0) 100%),
      linear-gradient(90deg, #e7e4e2 0%, var(--curtain) 40%, #fafafa 100%);
  }

  .waves { position: absolute; left: 0; top: 0; width: 907px; height: 1200px; }

  .brand {
    position: absolute; left: 640px; top: 70px; width: 230px;
    display: flex; align-items: center; gap: 12px;
  }
  .brand-square { width: 34px; height: 34px; background: var(--plum); flex: none; }
  .brand-name { font-weight: 700; font-size: 26px; line-height: 1.1; color: var(--plum); }

  .headline { position: absolute; right: 42px; top: 200px; text-align: right; }
  .headline-lead { display: block; font-weight: 900; font-size: 58px; letter-spacing: 1px; color: var(--pink); line-height: 1; }
  .headline-mid { display: block; font-weight: 700; font-size: 31px; color: var(--plum); line-height: 1.35; }
  .headline-end { display: block; font-weight: 300; font-size: 62px; letter-spacing: 2px; color: var(--ink); line-height: 1; }

  .copy { position: absolute; left: 72px; width: 520px; }
  .copy h2 { font-weight: 700; font-size: 30px; color: var(--pink); margin-bottom: 10px; }
  .copy p { font-size: 13.5px; line-height: 19px; color: var(--ink); }
  .copy-product { top: 622px; }
  .copy-about { top: 790px; }

  .product-shot { position: absolute; }

  .contact { position: absolute; left: 72px; top: 1080px; color: var(--paper); }
  .contact-phone { font-weight: 900; font-size: 36px; letter-spacing: 0.5px; margin-bottom: 12px; }
  .contact-line { display: flex; align-items: center; gap: 10px; font-size: 14px; line-height: 24px; }
  .contact-line svg { flex: none; }
</style>
</head>
<body>
<main class="flyer">
  <div class="hero-photo" role="img" aria-label="Photograph of a woman seen from behind fastening a black bra, against a white curtain"></div>

  <svg class="waves" viewBox="0 0 907 1200" aria-hidden="true">
    <!-- upper band -->
    <path d="M0 520 C 250 610, 560 560, 907 430 L907 1200 L0 1200 Z" fill="var(--plum)"/>
    <path d="M0 545 C 250 635, 560 585, 907 475 L907 1200 L0 1200 Z" fill="var(--paper)"/>
    <path d="M0 490 C 230 590, 540 560, 907 470 L907 490 C 560 590, 250 625, 0 520 Z" fill="var(--pink)"/>
    <path d="M0 560 C 260 650, 570 600, 907 500 L907 508 C 570 610, 260 662, 0 572 Z" fill="var(--plum)" opacity="0.9"/>
    <!-- lower band -->
    <path d="M0 1050 C 250 990, 560 1000, 907 1010 L907 1200 L0 1200 Z" fill="var(--pink)"/>
    <path d="M0 1070 C 260 1015, 570 1025, 907 1030 L907 1200 L0 1200 Z" fill="var(--plum)"/>
  </svg>

  <div class="brand">
    <span class="brand-square"></span>
    <span class="brand-name">Tarvel Apparel Company</span>
  </div>

  <h1 class="headline">
    <span class="headline-lead">INVISIBLE</span>
    <span class="headline-mid">SEAMS FOR IMPROVED</span>
    <span class="headline-end">COMFORT</span>
  </h1>

  <svg class="product-shot" style="left:555px; top:370px" width="270" height="270" viewBox="0 0 270 270" role="img" aria-label="Product photo: back view of the bra on a dress form showing pink straps and hook-and-eye fastener">
    <defs><radialGradient id="shotBack"><stop offset="0" stop-color="#e9e2dc"/><stop offset="0.6" stop-color="#cfc7c1"/><stop offset="1" stop-color="#8e8690"/></radialGradient></defs>
    <circle cx="135" cy="135" r="132" fill="var(--plum)"/>
    <circle cx="135" cy="135" r="120" fill="var(--paper)"/>
    <circle cx="135" cy="135" r="114" fill="var(--pink)"/>
    <circle cx="135" cy="135" r="106" fill="url(#shotBack)"/>
  </svg>

  <svg class="product-shot" style="left:690px; top:620px" width="216" height="216" viewBox="0 0 216 216" role="img" aria-label="Product photo: front view of the all-black bra on a dress form">
    <defs><radialGradient id="shotFront"><stop offset="0" stop-color="#3a3a3c"/><stop offset="0.45" stop-color="#d8d2cc"/><stop offset="1" stop-color="#e9e5e1"/></radialGradient></defs>
    <circle cx="108" cy="108" r="106" fill="var(--plum)"/>
    <circle cx="108" cy="108" r="96" fill="var(--paper)"/>
    <circle cx="108" cy="108" r="91" fill="var(--pink)"/>
    <circle cx="108" cy="108" r="84" fill="url(#shotFront)"/>
  </svg>

  <svg class="product-shot" style="left:660px; top:810px" width="240" height="240" viewBox="0 0 240 240" role="img" aria-label="Product photo: front view of the black bra with pink trim on a dress form">
    <defs><radialGradient id="shotTrim"><stop offset="0" stop-color="#2b2a2c"/><stop offset="0.5" stop-color="#b9aeb0"/><stop offset="1" stop-color="#e6e1dd"/></radialGradient></defs>
    <circle cx="120" cy="120" r="118" fill="var(--plum)"/>
    <circle cx="120" cy="120" r="107" fill="var(--paper)"/>
    <circle cx="120" cy="120" r="101" fill="var(--pink)"/>
    <circle cx="120" cy="120" r="94" fill="url(#shotTrim)"/>
  </svg>

  <section class="copy copy-product">
    <h2>Product description</h2>
    <p>Microfiber T-shirt bra with molded, lightly padded underwire cups for shaping and good support the bra also give's a fuller, uplifted shape and enhanced cleavage . Invisible seams for improved comfort. Narrow, adjustable shoulder straps and hook-and-eye fasteners at back. Available in two colors of Black &amp; Black with Decorative Touches of Pink.</p>
  </section>

  <section class="copy copy-about">
    <h2>About Tarvel Apparel Company</h2>
    <p>The Tarvel Apparel Company was founded on the philosophy of design, quality and the ideals of redefining fashion. Sri Lanka is the global hub for manufacturing some of the most exclusive and fashionable products and the Tarvel brand aims at giving the Sri Lankan consumer access to high-quality, affordable and fashionable clothing from a trusted company and name. A company-wide devotion to high quality, honest values and timeless style with a twist. That's authentic Tarvel. And that's just what you'll get, no matter your latitude or longitude. At Tarvel Apparel Company we constantly strive to build a culture just as inspiring as the people who wear our clothes</p>
  </section>

  <footer class="contact">
    <div class="contact-phone">+94 77 418 2093</div>
    <div class="contact-line">
      <svg width="16" height="12" viewBox="0 0 16 12" aria-hidden="true"><rect x="0.75" y="0.75" width="14.5" height="10.5" fill="none" stroke="var(--pink)" stroke-width="1.5"/><path d="M1 1 L8 7 L15 1" fill="none" stroke="var(--pink)" stroke-width="1.5"/></svg>
      <span>hello@tarvelapparel.com</span>
    </div>
    <div class="contact-line">
      <svg width="16" height="16" viewBox="0 0 16 16" aria-hidden="true"><circle cx="8" cy="8" r="6.5" fill="none" stroke="var(--pink)" stroke-width="1.5"/><path d="M1.5 8 H14.5 M8 1.5 C4.5 5, 4.5 11, 8 14.5 M8 1.5 C11.5 5, 11.5 11, 8 14.5" fill="none" stroke="var(--pink)" stroke-width="1.2"/></svg>
      <span>www.tarvelapparel.com</span>
    </div>
  </footer>
</main>
</body>
</html>
```